Paper Orchards (instructional dating book)

Title: Paper Orchards
Subtitle: Ways to charm a stranger across any crowded room
Author: R.J. Pollard
I'm seeking the title to be central with the subtitle underneath and the author slightly lower and to the left. Perhaps a border or two around the font. I thought the background could look aged (off color and old textured paper) and the background slightly punched into the texture like a typewriter has been used. I imagine it something like an old Fenwright playbook or 1940s morse code manual. Many thanks!

Target Market(s)

18 to 45 year old single people

Industry/Entity Type

Dating

Font styles to use
Serif

Requirements
Must have
• Text with border or two
Nice to have
• Traditional feel. The book is instructional.
Should not have
• Too much color or flair

```html
<!DOCTYPE html>
<html lang="en">
<head>
<meta charset="utf-8">
<title>Paper Orchards — R.J. Pollard</title>
<link rel="stylesheet" href="https://fonts.googleapis.com/css2?family=Crimson+Pro:wght@400;500&family=Cormorant+Garamond:wght@500;600&display=swap">
<style>
  :root {
    --page-bg: #ffffff;
    --paper-light: #f3dcab;
    --paper-mid: #e2ba74;
    --paper-edge: #c48544;
    --paper-burn: #9c5a26;
    --stain-dark: rgba(150, 88, 36, 0.22);
    --stain-light: rgba(250, 236, 200, 0.45);
    --title-red: #7a2a22;
    --ink-dark: #2e2a26;
    --rule-ink: #5b4a3a;
    --frame-ink: rgba(110, 62, 34, 0.55);
  }
  * { margin: 0; padding: 0; box-sizing: border-box; }
  html, body {
    width: 1200px;
    height: 1200px;
    overflow: hidden;
    background: var(--page-bg);
  }
  .canvas {
    position: relative;
    width: 1200px;
    height: 1200px;
  }
  .book-cover {
    position: absolute;
    left: 210px;
    top: 60px;
    width: 780px;
    height: 1080px;
    overflow: hidden;
  }
  .paper-texture {
    position: absolute;
    inset: 0;
    background:
      radial-gradient(circle 60px at 12% 20%, var(--stain-dark), transparent 70%),
      radial-gradient(circle 90px at 85% 12%, var(--stain-dark), transparent 70%),
      radial-gradient(circle 70px at 78% 42%, var(--stain-dark), transparent 70%),
      radial-gradient(circle 110px at 20% 62%, var(--stain-dark), transparent 70%),
      radial-gradient(circle 80px at 88% 74%, var(--stain-dark), transparent 70%),
      radial-gradient(circle 100px at 35% 90%, var(--stain-dark), transparent 70%),
      radial-gradient(circle 50px at 60% 30%, var(--stain-dark), transparent 70%),
      radial-gradient(circle 120px at 40% 30%, var(--stain-light), transparent 70%),
      radial-gradient(circle 140px at 65% 60%, var(--stain-light), transparent 70%),
      radial-gradient(circle 90px at 30% 78%, var(--stain-light), transparent 70%),
      radial-gradient(ellipse 65% 55% at 52% 50%, var(--paper-light) 0%, rgba(243,220,171,0) 72%),
      radial-gradient(ellipse 105% 92% at 50% 50%, var(--paper-mid) 42%, var(--paper-edge) 82%, var(--paper-burn) 100%);
  }
  .text-frame {
    position: absolute;
    left: 70px;
    top: 200px;
    width: 640px;
    height: 800px;
    border: 2px solid var(--frame-ink);
  }
  .text-frame::after {
    content: "";
    position: absolute;
    inset: 10px;
    border: 1px solid var(--frame-ink);
  }
  .cover-title {
    position: absolute;
    left: 0;
    right: 0;
    top: 255px;
    text-align: center;
    font-family: "Crimson Pro", "Times New Roman", serif;
    font-weight: 500;
    color: var(--title-red);
    font-size: 160px;
    line-height: 150px;
    letter-spacing: -1px;
  }
  .cover-title .title-line { display: block; }
  .cover-subtitle {
    position: absolute;
    left: 0;
    right: 0;
    top: 600px;
    text-align: center;
    font-family: "Crimson Pro", "Times New Roman", serif;
    font-weight: 400;
    color: var(--ink-dark);
    font-size: 34px;
    line-height: 44px;
  }
  .subtitle-rule {
    position: absolute;
    left: 190px;
    width: 400px;
    top: 700px;
    height: 1px;
    background: var(--rule-ink);
  }
  .cover-author {
    position: absolute;
    left: 150px;
    top: 850px;
    font-family: "Cormorant Garamond", "Times New Roman", serif;
    font-weight: 600;
    color: var(--ink-dark);
    font-size: 54px;
    letter-spacing: 5px;
    text-transform: uppercase;
  }
</style>
</head>
<body>
  <main class="canvas">
    <section class="book-cover">
      <div class="paper-texture" role="img" aria-label="Aged, stained and mottled parchment paper texture"></div>
      <div class="text-frame"></div>
      <h1 class="cover-title">
        <span class="title-line">Paper</span>
        <span class="title-line">Orchards</span>
      </h1>
      <p class="cover-subtitle">Ways to charm a stranger<br>across any crowded room</p>
      <div class="subtitle-rule"></div>
      <p class="cover-author">R.J. Pollard</p>
    </section>
  </main>
</body>
</html>
```